Website Redesign for Mortgage, Property and Conveyancing business

Project Overview:
We are looking for a refresh and redesign of our current website to a smart, crisp and fresh approach to Home Loans, Conveyancing and Property sales. This task will be to:
- Redesign our current website in accordance with the new wireframe.
- Provide all elements required for the design
- Build 7 key templates including:
Home Page
2nd Level Section Page
3rd level Product landing Page
2nd Level - About Us, Contact Us etc
Blog
Blog Article
Campaign Page - no header
Technical
The design is for a Wordpress website. Existing theme is Quillnest and we use Elementor for page editing. We are open to a new theme to be introduced but would prefer to stay with elementor.
Current Site is: www.corvanta.com.au
Sites that we like or elements of sites:
Pelham Real Estate: https://www.pelham-example.com.au/ (Like use of video and navigation)
Copper Lantern Lane - Mortage: https://cll-example.com.au/refinance-home-loan/ (Like landing pages a sin example)
Marquetry: https://marquetry-example.com.au/ (like Our services section).
Industry/Entity Type
Mortgage, Property, Conveyancing, Property Investment
Coding
Coded - Design and coding required
Number of Pages Required
5+ page
Font styles to use
Requirements
Must have
- Built for Wordpress and Elementor.
Nice to have
- See Project Description for links to ideas/elements that we have liked. However, open to ideas as long as the follow the navigation set out in the wire frame.

```html
<!DOCTYPE html>
<html lang="en">
<head>
<meta charset="utf-8">
<title>Corvanta – Finance, Property and Conveyancing</title>
<link href="https://fonts.googleapis.com/css2?family=Poppins:wght@300;400;500;600;700&display=swap" rel="stylesheet">
<style>
:root{
  --green:#0b9a3e;
  --blue:#26379b;
  --blue-dark:#1d2a80;
  --mint:#edf9f0;
  --text:#4a4a4a;
  --white:#ffffff;
  --line:#dcdcdc;
}
*{box-sizing:border-box;margin:0;padding:0}
html,body{width:1200px;height:4644px;overflow:hidden}
body{font-family:"Poppins",sans-serif;color:var(--text);background:var(--white)}
section,header,footer{position:relative;width:1200px;overflow:hidden}
.abs{position:absolute}
.btn{position:absolute;display:flex;align-items:center;justify-content:center;border-radius:40px;color:var(--white);font-weight:500;text-transform:uppercase}

/* header */
.site-header{height:135px;background:var(--white)}
.brand{left:87px;top:48px;display:flex;align-items:center;gap:10px}
.brand-mark{width:38px;height:38px;background:var(--blue)}
.brand-name{font-size:34px;font-weight:500;color:var(--blue);letter-spacing:-0.5px}
.nav{right:86px;top:84px;display:flex;gap:22px;font-size:13.5px;color:#444}
.top-phone{left:775px;top:31px;width:177px;height:38px;background:var(--blue);font-size:13px;gap:10px;text-transform:none;font-weight:400}
.top-phone i{width:30px;height:30px;border-radius:50%;background:var(--white);display:flex;align-items:center;justify-content:center;margin-left:-14px}
.top-contact{left:960px;top:31px;width:155px;height:38px;background:var(--green);font-size:13px}

/* hero */
.hero{height:745px}
.hero-photo{inset:0;background:linear-gradient(100deg,#3a3c40 0%,#55575b 35%,#6d6c68 60%,#47484b 100%)}
.hero-shade{inset:0;background:rgba(20,22,30,.45)}
.hero-title{top:218px;left:0;width:1200px;text-align:center;color:var(--white);font-size:56px;font-weight:500;line-height:66px}
.hero-sub{top:367px;left:0;width:1200px;text-align:center;color:var(--white);font-size:17px;line-height:28px}
.hero-btn{left:460px;top:470px;width:280px;height:64px;background:var(--blue);font-size:19px}
.dots{top:604px;left:555px;display:flex;gap:4px}
.dots span{width:15px;height:15px;border-radius:50%;border:1.5px solid var(--white)}
.dots span.on{background:var(--white)}
.hero-edge{left:0;bottom:0}

/* features */
.features{height:592px}
.feature{top:84px;width:328px;height:400px;background:var(--white);box-shadow:0 2px 10px rgba(0,0,0,.14);text-align:center;padding:34px 26px 0}
.feature.g{border-bottom:5px solid var(--green)}
.feature.b{border-bottom:5px solid var(--blue)}
.icon-ring{width:92px;height:92px;border-radius:50%;margin:0 auto;display:flex;align-items:center;justify-content:center;border:3px solid}
.icon-ring.g{border-color:var(--green)}
.icon-ring.b{border-color:var(--blue)}
.icon-ring i{width:76px;height:76px;border-radius:50%;display:flex;align-items:center;justify-content:center}
.icon-ring.g i{background:var(--green)}
.icon-ring.b i{background:var(--blue)}
.feature h3{margin-top:20px;font-size:21.5px;font-weight:500;line-height:30px;text-transform:uppercase}
.feature.g h3{color:var(--green)}
.feature.b h3{color:var(--blue)}
.feature p{margin-top:14px;font-size:14.5px;line-height:26px;text-align:justify;text-align-last:center}

/* headings */
.section-title{left:0;width:1200px;text-align:center;font-size:46px;font-weight:600;text-transform:uppercase}
.section-title .g{color:var(--green)}
.section-title .b{color:var(--blue)}

/* services */
.services{height:633px;background:var(--mint)}
.service{top:256px;width:326px;height:240px}
.service-photo{inset:0}
.service-icon{top:-56px;left:113px;width:100px;height:100px;border-radius:50%;background:var(--white);display:flex;align-items:center;justify-content:center}
.service-icon i{width:84px;height:84px;border-radius:50%;display:flex;align-items:center;justify-content:center}
.service-label{top:205px;left:28px;width:270px;height:70px;background:var(--white);display:flex;align-items:center;justify-content:center;font-size:16px;font-weight:500;color:var(--green);text-transform:uppercase;box-shadow:0 2px 8px rgba(0,0,0,.08)}
.service-label.active{background:var(--blue);color:var(--white);left:26px;width:300px}
.arrow{width:34px;height:34px;border-radius:50%;display:flex;align-items:center;justify-content:center}
.arrow.grey{background:#8b8b8b}
.arrow.green{background:var(--green)}

/* conveyancing band */
.convey{height:605px;background:linear-gradient(100deg,var(--blue-dark),var(--blue) 60%,#2d3fa6)}
.convey h2{left:87px;top:125px;width:660px;color:var(--white);font-size:47px;font-weight:600;line-height:58px}
.convey p{left:89px;top:285px;width:580px;color:var(--white);font-size:15px;line-height:26px}
.convey-btn{left:87px;top:403px;width:254px;height:74px;background:var(--green);font-size:18px}
.convey-art{left:760px;top:92px;width:440px;height:420px;border-radius:50% 0 0 50%/60% 0 0 40%;background:radial-gradient(circle at 40% 40%,#bfe6e8 0%,#7fbfc6 35%,#e2a78a 70%,rgba(38,55,155,0) 72%)}
.convey-edge{left:0;bottom:0}

/* testimonials */
.testimonials{height:652px}
.review{top:218px;width:318px;height:320px;background:var(--white);box-shadow:0 2px 12px rgba(0,0,0,.12);padding:36px 38px 0 38px}
.quote{position:absolute;left:-26px;top:44px;width:52px;height:52px;border-radius:50%;display:flex;align-items:center;justify-content:center}
.stars{display:flex;gap:4px}
.review p{margin-top:14px;font-size:14.5px;line-height:22px;text-align:justify}
.review hr{border:0;border-top:1px solid var(--line);margin-top:26px}
.reviewer{display:flex;align-items:center;gap:14px;margin-top:20px;font-size:15px;font-weight:600;color:#222}
.avatar{width:66px;height:66px;border-radius:50%;background:linear-gradient(135deg,#c9c2bb,#8d8680)}

/* contact */
.contact{height:674px;background:var(--mint)}
.info{top:247px;display:flex;align-items:center;gap:22px}
.info-circle{width:84px;height:84px;border-radius:50%;background:var(--white);box-shadow:0 2px 10px rgba(0,0,0,.1);display:flex;align-items:center;justify-content:center}
.info h4{font-size:22px;font-weight:500;color:#222;line-height:28px}
.info span{font-size:14.5px;color:#333}
.field{position:absolute;background:var(--white);border:1px solid #d4dcd6;height:50px;font-size:14px;color:#999;padding:14px 22px}
.submit{left:504px;top:569px;width:192px;height:58px;background:var(--green);font-size:19px;text-transform:uppercase}

/* footer */
.site-footer{height:608px;background:linear-gradient(180deg,var(--blue) 0%,#2b3d9f 45%,var(--blue) 100%)}
.footer-logo{left:0;top:148px;width:1200px;display:flex;justify-content:center;align-items:center;gap:10px}
.footer-logo .brand-mark{background:var(--white)}
.footer-logo .brand-name{color:var(--white)}
.fcol{top:226px;color:var(--white);font-size:14.5px}
.fcol h5{font-size:16.5px;font-weight:500;margin-bottom:42px}
.fcol p{line-height:24px;margin-bottom:20px}
.links li{list-style:none;line-height:31px}
.links li::before{content:"›";color:var(--green);margin-right:12px;font-weight:600}
.crow{display:flex;gap:24px;margin-bottom:14px;line-height:20px}
.crow i{width:26px;height:26px;background:var(--green);display:flex;align-items:center;justify-content:center;flex-shrink:0;margin-top:4px}
.news-input{width:250px;height:38px;background:var(--white);margin-top:8px}
.news-btn{margin-top:10px;width:126px;height:38px;background:var(--green);display:flex;align-items:center;justify-content:center;font-size:12.5px;text-transform:uppercase}
.legal{right:86px;top:509px;color:var(--white);font-size:10.5px;text-transform:uppercase}
.bottom-bar{left:0;top:541px;width:1200px;height:67px;background:var(--green);color:var(--white);font-size:13.5px}
.bottom-bar .copy{left:87px;top:24px}
.social{top:15px;width:34px;height:34px;background:var(--blue)}
</style>
</head>
<body>

<header class="site-header">
  <div class="abs brand"><span class="brand-mark"></span><span class="brand-name">Corvanta</span></div>
  <div class="btn top-phone"><i><svg width="16" height="16" viewBox="0 0 24 24"><path fill="#26379b" d="M6.6 10.8c1.4 2.8 3.8 5.1 6.6 6.6l2.2-2.2c.3-.3.7-.4 1-.2 1.1.4 2.3.6 3.6.6.6 0 1 .4 1 1V20c0 .6-.4 1-1 1C10.6 21 3 13.4 3 4c0-.6.4-1 1-1h3.5c.6 0 1 .4 1 1 0 1.3.2 2.5.6 3.6.1.3 0 .7-.2 1z"/></svg></i>904-555-0147</div>
  <div class="btn top-contact">Contact Us</div>
  <nav class="abs nav"><span>Finance</span><span>Property Investment</span><span>Property Purchase &amp; Sales</span><span>Property Management</span><span>Conveyancing</span><span>About</span></nav>
</header>

<section class="hero">
  <div class="abs hero-photo" role="img" aria-label="Photo of a couple meeting with a financial adviser at a desk"></div>
  <div class="abs hero-shade"></div>
  <h1 class="abs hero-title">We’re here to help you<br>increase your financial wellbeing</h1>
  <p class="abs hero-sub">Integrated finance, conveyancing, property investment and property management<br>along with accounting solutions.</p>
  <div class="btn hero-btn">Know More</div>
  <div class="abs dots"><span></span><span></span><span class="on"></span><span></span><span></span></div>
  <svg class="abs hero-edge" width="1200" height="112" viewBox="0 0 1200 112">
    <polygon points="0,98 1200,8 1200,112 0,112" fill="#fff"/>
    <polygon points="157,95 1200,8 1200,30 157,112" fill="#0b9a3e"/>
  </svg>
</section>

<section class="features">
  <article class="abs feature g" style="left:87px">
    <div class="icon-ring g"><i><svg width="40" height="40" viewBox="0 0 40 40" fill="none" stroke="#fff" stroke-width="2"><circle cx="12" cy="16" r="4"/><circle cx="28" cy="16" r="4"/><circle cx="20" cy="24" r="4"/><path d="M6 34c0-4 3-7 6-7M34 34c0-4-3-7-6-7M13 38c0-4 3-7 7-7s7 3 7 7"/><path d="M20 5l1.5 3 3 .4-2.2 2 .6 3-2.9-1.5-2.9 1.5.6-3-2.2-2 3-.4z"/></svg></i></div>
    <h3>We have 20 years<br>experience</h3>
    <p>We have grown and changed with the industry and we’re dedicated to continually improve our service and products so you get the best solutions possible.</p>
  </article>
  <article class="abs feature b" style="left:437px">
    <div class="icon-ring b"><i><svg width="40" height="40" viewBox="0 0 40 40" fill="none" stroke="#fff" stroke-width="2"><rect x="9" y="6" width="20" height="28" rx="1"/><path d="M13 13h12M13 18h12M13 23h7"/><circle cx="28" cy="29" r="6"/><path d="M25 29l2 2 4-4"/></svg></i></div>
    <h3>We care about the<br>outcome</h3>
    <p>When we say we care, we mean it. If you are a client now, we want you to be a happy client. If we can’t help you become a client today we’d like to help you tomorrow.</p>
  </article>
  <article class="abs feature g" style="left:787px">
    <div class="icon-ring g"><i><svg width="40" height="40" viewBox="0 0 40 40" fill="none" stroke="#fff" stroke-width="2"><path d="M6 18L20 7l14 11"/><path d="M10 16v16h20V16"/><circle cx="20" cy="20" r="3"/><path d="M14 32c0-4 3-6 6-6s6 2 6 6"/></svg></i></div>
    <h3>We give options that<br>makes sense</h3>
    <p>Our team of finance, property investment and accounting experts know what they are talking about and they are happy to take the time to explain things clearly.</p>
  </article>
</section>

<section class="services">
  <h2 class="abs section-title" style="top:128px"><span class="g">Our</span> <span class="b">Services</span></h2>
  <div class="abs arrow grey" style="left:26px;top:364px"><svg width="12" height="12" viewBox="0 0 12 12"><path d="M8 2L4 6l4 4" stroke="#fff" stroke-width="2" fill="none"/></svg></div>
  <div class="abs arrow green" style="left:1140px;top:364px"><svg width="12" height="12" viewBox="0 0 12 12"><path d="M4 2l4 4-4 4" stroke="#fff" stroke-width="2" fill="none"/></svg></div>

  <div class="abs service" style="left:86px">
    <div class="abs service-photo" role="img" aria-label="Photo of a hand holding a bank card by a laptop" style="background:linear-gradient(135deg,#e9ecef,#c7cdd3 50%,#5b87c6)"></div>
    <div class="abs service-icon"><i style="background:var(--green)"><svg width="36" height="36" viewBox="0 0 24 24"><path fill="#fff" d="M12 3L2 12h3v8h5v-5h4v5h5v-8h3z"/></svg></i></div>
    <div class="abs service-label">Finance</div>
  </div>
  <div class="abs service" style="left:439px">
    <div class="abs service-photo" role="img" aria-label="Photo of a smiling couple with an agent" style="background:linear-gradient(135deg,#b8c59c,#d9c4a6 45%,#3a3d45)"></div>
    <div class="abs service-icon"><i style="background:var(--blue)"><svg width="36" height="36" viewBox="0 0 24 24" fill="none" stroke="#fff" stroke-width="1.5"><path d="M4 11l8-7 8 7"/><path d="M6 10v9h12v-9"/><circle cx="12" cy="14" r="2.5"/><path d="M12 12.5v3"/></svg></i></div>
    <div class="abs service-label active">Property Investment</div>
  </div>
  <div class="abs service" style="left:790px">
    <div class="abs service-photo" role="img" aria-label="Photo of a modern white house with trees" style="background:linear-gradient(135deg,#dfe3e2,#f1f1ef 45%,#5e7250)"></div>
    <div class="abs service-icon"><i style="background:var(--green)"><svg width="36" height="36" viewBox="0 0 24 24" fill="none" stroke="#fff" stroke-width="1.5"><rect x="6" y="3" width="12" height="17"/><path d="M9 8h6M9 12h6M9 16h3"/></svg></i></div>
    <div class="abs service-label">Property Management</div>
  </div>
</section>

<section class="convey">
  <h2 class="abs">Making your property sale or purchase safe and easy</h2>
  <p class="abs">We understand the importance of an efficient and easy to understand conveyancer when buying or selling a property. For a cost effective and smooth settlement speak to our Senior Conveyancer today.</p>
  <div class="btn convey-btn">Contact Us Now</div>
  <div class="abs convey-art" role="img" aria-label="Illustration of a hand holding a house inside a glass sphere"></div>
  <svg class="abs convey-edge" width="1200" height="80" viewBox="0 0 1200 80">
    <polygon points="0,72 1200,10 1200,80 0,80" fill="#fff"/>
    <polygon points="153,58 1200,0 1200,22 153,80" fill="#0b9a3e"/>
  </svg>
</section>

<section class="testimonials">
  <h2 class="abs section-title" style="top:112px"><span class="g">What our</span> <span class="b">Clients says</span></h2>
  <div class="abs arrow grey" style="left:26px;top:394px"><svg width="12" height="12" viewBox="0 0 12 12"><path d="M8 2L4 6l4 4" stroke="#fff" stroke-width="2" fill="none"/></svg></div>
  <div class="abs arrow green" style="left:1140px;top:394px"><svg width="12" height="12" viewBox="0 0 12 12"><path d="M4 2l4 4-4 4" stroke="#fff" stroke-width="2" fill="none"/></svg></div>

  <article class="abs review" style="left:90px">
    <div class="quote" style="background:var(--green)"><svg width="24" height="20" viewBox="0 0 24 20"><path fill="#fff" d="M0 20V11C0 5 3 1 9 0v4c-3 1-4 3-4 6h4v10zM14 20V11c0-6 3-10 9-11v4c-3 1-4 3-4 6h4v10z"/></svg></div>
    <div class="stars"><svg width="100" height="14" viewBox="0 0 100 14"><g fill="#f2b701"><path id="s" d="M7 0l2 4.5 5 .5-3.8 3.3 1.1 4.9L7 10.7 2.7 13.2l1.1-4.9L0 5l5-.5z"/><use href="#s" x="20"/><use href="#s" x="40"/><use href="#s" x="60"/><use href="#s" x="80"/></g></svg></div>
    <p>Lorem ipsum dolor sit amet, conse ctetuer adipiscing elit. Aenean comodo ligula eget dolor. Aenean massa. Cum sociis</p>
    <hr>
    <div class="reviewer"><span class="avatar" role="img" aria-label="Client portrait"></span>Marcus Feld</div>
  </article>
  <article class="abs review" style="left:445px">
    <div class="quote" style="background:var(--blue)"><svg width="24" height="20" viewBox="0 0 24 20"><path fill="#fff" d="M0 20V11C0 5 3 1 9 0v4c-3 1-4 3-4 6h4v10zM14 20V11c0-6 3-10 9-11v4c-3 1-4 3-4 6h4v10z"/></svg></div>
    <div class="stars"><svg width="100" height="14" viewBox="0 0 100 14"><g fill="#f2b701"><use href="#s"/><use href="#s" x="20"/><use href="#s" x="40"/><use href="#s" x="60"/><use href="#s" x="80"/></g></svg></div>
    <p>Lorem ipsum dolor sit amet, conse ctetuer adipiscing elit. Aenean comodo ligula eget dolor. Aenean massa. Cum sociis</p>
    <hr>
    <div class="reviewer"><span class="avatar" role="img" aria-label="Client portrait"></span>Oliver Brant</div>
  </article>
  <article class="abs review" style="left:801px">
    <div class="quote" style="background:var(--green)"><svg width="24" height="20" viewBox="0 0 24 20"><path fill="#fff" d="M0 20V11C0 5 3 1 9 0v4c-3 1-4 3-4 6h4v10zM14 20V11c0-6 3-10 9-11v4c-3 1-4 3-4 6h4v10z"/></svg></div>
    <div class="stars"><svg width="100" height="14" viewBox="0 0 100 14"><g fill="#f2b701"><use href="#s"/><use href="#s" x="20"/><use href="#s" x="40"/><use href="#s" x="60"/><use href="#s" x="80"/></g></svg></div>
    <p>Lorem ipsum dolor sit amet, conse ctetuer adipiscing elit. Aenean comodo ligula eget dolor. Aenean massa. Cum sociis</p>
    <hr>
    <div class="reviewer"><span class="avatar" role="img" aria-label="Client portrait"></span>Tobias Reyne</div>
  </article>
</section>

<section class="contact">
  <h2 class="abs section-title" style="top:128px"><span class="g">Get in</span> <span class="b">Touch</span></h2>
  <div class="abs info" style="left:112px">
    <div class="info-circle"><svg width="40" height="40" viewBox="0 0 24 24"><path fill="#0b9a3e" d="M6.6 10.8c1.4 2.8 3.8 5.1 6.6 6.6l2.2-2.2c.3-.3.7-.4 1-.2 1.1.4 2.3.6 3.6.6.6 0 1 .4 1 1V20c0 .6-.4 1-1 1C10.6 21 3 13.4 3 4c0-.6.4-1 1-1h3.5c.6 0 1 .4 1 1 0 1.3.2 2.5.6 3.6.1.3 0 .7-.2 1z"/></svg></div>
    <div><h4>CALL US</h4><span>8012 555 0193</span></div>
  </div>
  <div class="abs info" style="left:367px">
    <div class="info-circle"><svg width="42" height="30" viewBox="0 0 42 30"><rect x="1" y="1" width="40" height="28" fill="#26379b"/><path d="M1 1l20 16L41 1M1 29l15-14M41 29L26 15" stroke="#fff" stroke-width="2" fill="none"/></svg></div>
    <div><h4>EMAIL US</h4><span>info@corvanta.com.au</span></div>
  </div>
  <div class="abs info" style="left:690px">
    <div class="info-circle"><svg width="30" height="40" viewBox="0 0 24 32"><path fill="#0b9a3e" d="M12 0C5.4 0 0 5.4 0 12c0 9 12 20 12 20s12-11 12-20C24 5.4 18.6 0 12 0zm0 17a5 5 0 110-10 5 5 0 010 10z"/></svg></div>
    <div><h4>LOCATION</h4><span>42 Larchmont Close, Fernbrook, VIC 3199</span></div>
  </div>

  <div class="field" style="left:245px;top:328px;width:710px">Name:</div>
  <div class="field" style="left:245px;top:388px;width:345px">Phone:</div>
  <div class="field" style="left:610px;top:388px;width:345px">Email:</div>
  <div class="field" style="left:245px;top:449px;width:710px;height:95px">Mesage:</div>
  <div class="btn submit">Submit</div>
</section>

<footer class="site-footer" role="contentinfo">
  <div class="abs" role="img" aria-label="Faded photo of a suburban house behind the footer" style="inset:0;background:radial-gradient(ellipse at 50% 30%,rgba(255,255,255,.08),rgba(0,0,0,0) 60%)"></div>
  <div class="abs footer-logo"><span class="brand-mark"></span><span class="brand-name">Corvanta</span></div>

  <div class="abs fcol" style="left:88px">
    <h5>Operating Times</h5>
    <p>Monday to Friday:<br>9.00 AM – 5.00 PM</p>
    <p>Saturday &amp; Sunday:<br>Closed</p>
  </div>
  <div class="abs fcol" style="left:292px">
    <h5 style="margin-bottom:32px">Quick Links</h5>
    <ul class="links"><li>Finance</li><li>Property Investment</li><li>Property Purchase &amp; Sales</li><li>Property Management</li><li>Conveyancing</li><li>About</li><li>Contact Us</li></ul>
  </div>
  <div class="abs fcol" style="left:568px">
    <h5 style="margin-bottom:36px">Contact Us</h5>
    <div class="crow"><i><svg width="14" height="14" viewBox="0 0 24 24"><path fill="#fff" d="M6.6 10.8c1.4 2.8 3.8 5.1 6.6 6.6l2.2-2.2c.3-.3.7-.4 1-.2 1.1.4 2.3.6 3.6.6.6 0 1 .4 1 1V20c0 .6-.4 1-1 1C10.6 21 3 13.4 3 4c0-.6.4-1 1-1h3.5c.6 0 1 .4 1 1 0 1.3.2 2.5.6 3.6.1.3 0 .7-.2 1z"/></svg></i><span>CALL US<br>1300 555 217</span></div>
    <div class="crow"><i><svg width="14" height="10" viewBox="0 0 14 10"><rect width="14" height="10" fill="#fff"/><path d="M0 0l7 5 7-5" stroke="#0b9a3e" fill="none"/></svg></i><span>EMAIL US<br>info@corvanta.com.au</span></div>
    <div class="crow"><i><svg width="10" height="14" viewBox="0 0 24 32"><path fill="#fff" d="M12 0C5.4 0 0 5.4 0 12c0 9 12 20 12 20s12-11 12-20C24 5.4 18.6 0 12 0zm0 17a5 5 0 110-10 5 5 0 010 10z"/></svg></i><span>42 Larchmont Close, Fernbrook,<br>VIC 3199</span></div>
  </div>
  <div class="abs fcol" style="left:865px">
    <h5 style="margin-bottom:38px">Our Newsletter</h5>
    <p style="margin-bottom:10px">Subscribe our newsletter to get<br>the latest news.</p>
    <div class="news-input"></div>
    <div class="news-btn">Subscribe</div>
  </div>

  <div class="abs legal">Home | Why Corvanta | Contact Us | Privacy Policy | Privacy Consent &amp; Credit Guide | Dispute Resolution</div>

  <div class="abs bottom-bar">
    <span class="abs copy">© 2024 Veltrane Pty Ltd - All Rights Reserved - ABN: 00 000 000 000</span>
    <span class="abs social" style="left:1039px"></span>
    <span class="abs social" style="left:1080px"></span>
  </div>
</footer>

</body>
</html>
```